Personal Care and Home care ingredients Brochure

We need a flyer or brochure of the of chemicals we distribute for the manufacturing of personal care products such as shampoos, liquid soaps, creams, lotions, conditioners, hand sanitizer, Hair Jellys, etc and for Home care products such as, liquid soaps, desinfectants, cleaners, stain removers,etc.
The idea is to send this pdf brochure via email and companies feel very confortable with the impression it gives. We want to call attention.
Target Market(s)
Companies that manufactures cosmetics, personal care products and home care products.
Colors
Designer to choose colors to be used in the design.
Requirements
Must have
- Images that refers to the skin, hair, cleaning, washing

```html
<!DOCTYPE html>
<html lang="es">
<head>
<meta charset="utf-8">
<title>Palmivera – Ficha de ingrediente</title>
<link href="https://fonts.googleapis.com/css2?family=Montserrat:wght@400;800&family=Roboto+Condensed:wght@300;400;600;700&display=swap" rel="stylesheet">
<style>
  :root{
    --paper:#ffffff;
    --frame:#8e8e8e;
    --text:#8a8a8a;
    --heading:#7d7d7d;
    --teal:#2f9a78;
    --olive:#7b8c34;
    --water-dark:#16253a;
    --water-mid:#50647c;
    --water-light:#c9d3dc;
  }
  *{margin:0;padding:0;box-sizing:border-box}
  html,body{width:1200px;height:1200px;overflow:hidden;background:var(--paper)}
  body{position:relative;font-family:"Roboto Condensed",sans-serif;color:var(--text)}
  .panel{position:absolute;border:2px solid var(--frame);background:var(--paper);overflow:hidden}
  .panel--intro{left:61px;top:140px;width:1086px;height:418px}
  .panel--guide{left:51px;top:619px;width:1107px;height:418px}

  .hero-photo{position:absolute;left:0;top:0;width:654px;height:100%;
    background:linear-gradient(90deg,var(--water-dark) 0%,#2a3c55 35%,var(--water-mid) 62%,var(--water-light) 80%,#6f8297 100%)}
  .hero-title{position:absolute;left:44px;top:315px;color:#fff}
  .hero-title h1{font-family:"Montserrat",sans-serif;font-weight:800;font-size:35px;letter-spacing:.5px;line-height:1}
  .hero-title p{font-family:"Montserrat",sans-serif;font-weight:400;font-size:15px;margin-top:2px}

  .tree{position:absolute;left:0;top:0}
  .tree-label{position:absolute;top:124px;font-weight:600;font-size:12.5px;color:var(--teal);white-space:nowrap}
  .tree-label--left{right:220px}
  .tree-label--right{left:875px}

  .benefits{position:absolute;top:176px;font-size:11.6px;line-height:20.6px;font-weight:300;letter-spacing:-.1px}
  .benefits h2{font-weight:600;font-size:11.6px;color:var(--heading);margin-bottom:20.6px;line-height:20.6px;letter-spacing:-.1px}
  .benefits--labsa{left:670px;width:206px}
  .benefits--sles{left:885px;width:190px}
  .benefits--sles h2{margin-bottom:0}

  .notes{position:absolute;top:54px;font-size:11.6px;line-height:20.6px;font-weight:300;letter-spacing:-.1px}
  .notes--left{left:39px;width:230px}
  .notes--right{left:292px;width:250px}
  .notes h2{font-weight:400;font-size:11.6px;color:var(--heading)}
  .divider{position:absolute;left:275px;top:0;height:100%;border-left:1.5px dotted var(--frame)}

  .range-photo{position:absolute;left:552px;top:0;width:553px;height:100%;
    background:linear-gradient(108deg,#d9cfc2 0%,#b5472f 25%,#2f4f7a 40%,#c76a37 56%,#d8c64a 59%,#4f9a37 78%,#2f8a3a 100%)}
  .range-title{position:absolute;left:598px;top:281px;font-family:"Montserrat",sans-serif;font-weight:800;
    font-size:32px;line-height:37px;color:#fff;text-shadow:0 0 6px rgba(0,0,0,.55);white-space:nowrap}
</style>
</head>
<body>
  <section class="panel panel--intro">
    <div class="hero-photo" role="img" aria-label="Salpicaduras de agua cristalina sobre fondo azul oscuro"></div>
    <div class="hero-title">
      <h1>PALMIVERA</h1>
      <p>Seguridad y Suavidad.</p>
    </div>

    <svg class="tree" width="1086" height="418" viewBox="0 0 1086 418">
      <rect x="854" y="46" width="34" height="16" rx="8" fill="var(--teal)"/>
      <text x="871" y="58" text-anchor="middle" font-family="Roboto Condensed, sans-serif" font-size="11.5" font-weight="600" fill="#fff">MES</text>
      <g stroke="var(--olive)" stroke-width="1.6" stroke-dasharray="1.6 3" fill="none">
        <line x1="871" y1="66" x2="871" y2="144"/>
        <line x1="760" y1="144" x2="980" y2="144"/>
        <line x1="760" y1="144" x2="760" y2="152"/>
        <line x1="980" y1="144" x2="980" y2="152"/>
      </g>
      <polygon points="754,154 766,154 760,164" fill="var(--olive)"/>
      <polygon points="974,154 986,154 980,164" fill="var(--olive)"/>
    </svg>
    <span class="tree-label tree-label--left">Reemplazo de LABSA</span>
    <span class="tree-label tree-label--right">Reemplazo de SLES</span>

    <div class="benefits benefits--labsa">
      <h2>LAVAPLATOS LIQUIDOS Y DETERGENTES<br>LIQUIDOS DE LAVANDERIA</h2>
      <p>* Más suave para la piel</p>
      <p>* Ingrediente Alternativo a Productos<br>derivados del Pétroleo</p>
      <p>* Mejor detergencia en Agua Dura.</p>
      <p>* Mejor remoción de manchas de aceite.</p>
      <p>* Uso de productos naturales derivados de<br>la palma.</p>
    </div>
    <div class="benefits benefits--sles">
      <h2>LAVAPLATOS LIQUIDOS / DETERGENTES<br>LIQUIDOS / JABANO DE TOCADOR<br>LIQUIDO</h2>
      <p>* Menor costo de materia prima por<br>unidad activa.</p>
      <p>* Desempeño similar</p>
      <p>* Suavidad similar al SLES</p>
    </div>
  </section>

  <section class="panel panel--guide">
    <div class="notes notes--left">
      <p>* El MES no necesita neutralizacion, y al diluir la solicion ya esta activa.</p>
      <p>* Se recomienda 30-50% de LABSA y no un reemplazo total para lograr un efecto sinergistico.</p>
      <p>* Comparado con el LABSA, el MES es mas suave para la piel, un tiene efecto de limpieza mas fuerte sobre manchas de grasas vegetales/oleosas y un mayor poder de detergencia en aguas con alto contenido de dureza.</p>
    </div>
    <div class="divider"></div>
    <div class="notes notes--right">
      <h2>RECOMENDACIONES GENERALES</h2>
      <p>* Si se requiero que el liquido final lavaplatos/detergente sea transparente o cristalino, el maximo contenido de MES no debe ser mas de 5%.</p>
      <p>* A pesar que es posible reemplazar totalmente el LAS o LABSA, se recomienda la presencia de mas surfactantes para buscar un mejor efecto sinergistico.</p>
      <p>* MES no debe ser expuesto a pH menor de 5 o mayor de 9 por mas de 24 horas porque se degrada.</p>
      <p>* El uso de MES en productos liquidos requiere una dosis de ajuste de electrolito (Sal) para alcanzar la viscosidad deseada.</p>
    </div>
    <div class="range-photo" role="img" aria-label="Frascos de cosméticos junto a botellas de lavaplatos verde y amarillo"></div>
    <h2 class="range-title">PRODUCTOS PARA<br>CUIDADO PERSONAL Y<br>CUIDADO DEL HOGAR</h2>
  </section>
</body>
</html>
```